Telmoro Business Card

I already have the conplay logo. I need to develop a professional business card layout

Target Market(s)

Business

Industry/Entity Type

Business

Contact Information for Business Card

Company Name: Telmoro Limited

Font styles to use
Sans Serif

Colors

Designer to choose colors to be used in the design.

Requirements
Must have
• Use current logo
• Need two card size options:
• Small Card: 70mm x 28mm (Landscape)
• Square Card: 65mm x 65mm
Nice to have
• I will need 8-10 files for each name, number and email address (details to follow)

```html
<!DOCTYPE html>
<html lang="en">
<head>
<meta charset="utf-8">
<title>Telmoro Business Cards</title>
<link href="https://fonts.googleapis.com/css2?family=Lato:wght@400;700;900&display=swap" rel="stylesheet">
<style>
  :root {
    --backdrop: #3a3a3a;
    --card-white: #ffffff;
    --band-top: #2183c6;
    --band-bottom: #1157a9;
    --brand-blue: #1c6db8;
    --text-light: #ffffff;
  }
  * { margin: 0; padding: 0; box-sizing: border-box; }
  html, body {
    width: 1200px;
    height: 1200px;
    overflow: hidden;
    background: var(--backdrop);
    font-family: "Lato", sans-serif;
  }
  .canvas {
    position: relative;
    width: 1200px;
    height: 1200px;
  }
  .card {
    position: absolute;
    background: var(--card-white);
    box-shadow: 0 10px 28px rgba(0, 0, 0, 0.45);
    overflow: hidden;
  }
  .card--square { left: 145px; top: 328px; width: 574px; height: 574px; }
  .card--slim   { left: 830px; top: 314px; width: 226px; height: 631px; }

  .card__brand {
    position: absolute;
    left: 0; right: 0;
    text-align: center;
    font-weight: 900;
    color: var(--brand-blue);
    line-height: 1;
    letter-spacing: 1px;
  }
  .card--square .card__brand { top: 110px; font-size: 70px; }
  .card--slim .card__brand   { top: 126px; font-size: 36px; letter-spacing: 0; }

  .card__band {
    position: absolute;
    left: 0; right: 0; bottom: 0;
    background: linear-gradient(to bottom, var(--band-top), var(--band-bottom));
    color: var(--text-light);
    text-align: center;
  }
  .card--square .card__band { top: 290px; }
  .card--slim .card__band   { top: 295px; }

  .card__line {
    position: absolute;
    left: 0; right: 0;
    line-height: 1;
    white-space: nowrap;
  }
  .card__name  { font-weight: 700; }
  .card__title { font-weight: 700; }
  .card__contact { font-weight: 400; }

  /* square card text */
  .card--square .card__name    { top: 32px;  font-size: 33px; }
  .card--square .card__title   { top: 70px;  font-size: 20px; }
  .card--square .card__phone   { top: 152px; font-size: 20px; }
  .card--square .card__email   { top: 181px; font-size: 20px; }
  .card--square .card__address { top: 209px; font-size: 20px; }

  /* slim card text */
  .card--slim .card__name     { top: 62px;  font-size: 27px; }
  .card--slim .card__title    { top: 96px;  font-size: 20px; }
  .card--slim .card__phone    { top: 176px; font-size: 18px; }
  .card--slim .card__email    { top: 203px; font-size: 17px; }
  .card--slim .card__address1 { top: 259px; font-size: 18px; }
  .card--slim .card__address2 { top: 281px; font-size: 18px; }
</style>
</head>
<body>
<div class="canvas">

  <section class="card card--square" aria-label="Square business card">
    <div class="card__brand">TELMORO</div>
    <div class="card__band">
      <p class="card__line card__name">Martin Hale</p>
      <p class="card__line card__title">President</p>
      <p class="card__line card__contact card__phone">(555) 318 2047</p>
      <p class="card__line card__contact card__email">info@telmoro.com</p>
      <p class="card__line card__contact card__address">18 Harrow Lane, Westbrook NSW 2190</p>
    </div>
  </section>

  <section class="card card--slim" aria-label="Slim business card">
    <div class="card__brand">TELMORO</div>
    <div class="card__band">
      <p class="card__line card__name">Martin Hale</p>
      <p class="card__line card__title">President</p>
      <p class="card__line card__contact card__phone">(555) 318 2047</p>
      <p class="card__line card__contact card__email">info@telmoro.com</p>
      <p class="card__line card__contact card__address1">18 Harrow Lane,</p>
      <p class="card__line card__contact card__address2">Westbrook NSW 2190</p>
    </div>
  </section>

</div>
</body>
</html>
```